vireLattice "organisation chart"

We need a new Organisation Chart for our Company! We are actually in a Change-management-process and will Change from a hierarchical Organisation in to a Network Organisation. Therefor we need a new Organisation Chart.
The following departements must be visible and legible on the Chart:
Team Sales & Consulting
Team Productmanagement
Team Supply Chain
Team Human Resources
Team Smart Digital Development
Team Marketing & Communication
The title of the Chart ist «vireLattice»
The Colors of the back of the Chart must be: RGB 73/25/102 // Pantone 2627
The Colors for the different Teams should be:
Team Sales & Consulting (Pantone: 803/neon yellow = Background)
Team Productmanagement (Pantone: 804/neon orange = Background)
Team Supply Chain (Pantone: 802/neon green = Background)
Team Human Resources (Pantone: 801/neon blue = Background)
Team Smart Digital Development (Pantone: 805/neon red = Background)
Team Marketing & Communication (Pantone: 803/neon pink = Background)
See below (upload files) an example showing a self-made Chart ... :-)
Our font is: Univers LT Std // Please feel free to Combine the Fonts Colors with the background colors
It Company

```html
<!DOCTYPE html>
<html lang="en">
<head>
<meta charset="utf-8">
<title>vireLattice – Organisation Chart</title>
<link rel="stylesheet" href="https://fonts.googleapis.com/css2?family=Archivo:wght@700&family=Jost:wght@300&display=swap">
<style>
  :root {
    --bg-aubergine: #4a1966;
    --title-white: #ffffff;
    --link-pink: #ec2a9c;
    --team-sales: #d6de1f;
    --team-product: #f7941d;
    --team-supply: #8dc63f;
    --team-hr: #29abe2;
    --team-digital: #d81e5b;
    --team-marketing: #ec008c;
    --core-white: #ffffff;
    --label-ink: #1a1a1a;
  }
  html, body {
    margin: 0;
    padding: 0;
    overflow: hidden;
    background: var(--bg-aubergine);
  }
  .chart {
    display: block;
    width: 1200px;
    height: 1000px;
    background: var(--bg-aubergine);
  }
  .chart-title {
    font-family: "Jost", "Helvetica Neue", Arial, sans-serif;
    font-weight: 300;
    font-size: 80px;
    fill: var(--title-white);
    letter-spacing: 1px;
  }
  .team-ring { stroke-width: 20; fill: var(--core-white); }
  .team-sales .team-ring { stroke: var(--team-sales); }
  .team-product .team-ring { stroke: var(--team-product); }
  .team-supply .team-ring { stroke: var(--team-supply); }
  .team-hr .team-ring { stroke: var(--team-hr); }
  .team-digital .team-ring { stroke: var(--team-digital); }
  .team-marketing .team-ring { stroke: var(--team-marketing); }
  .team-label {
    font-family: "Archivo", "Helvetica Neue", Arial, sans-serif;
    font-weight: 700;
    font-size: 18px;
    fill: var(--label-ink);
    text-anchor: middle;
  }
  .link-arrow {
    fill: none;
    stroke: var(--link-pink);
    stroke-width: 8;
  }
  .hub-spoke {
    stroke: var(--link-pink);
    stroke-width: 12;
  }
  .arrow-head { fill: var(--link-pink); }
</style>
</head>
<body>
<svg class="chart" viewBox="0 0 1200 1000" width="1200" height="1000" role="img" aria-label="vireLattice network organisation chart">
  <defs>
    <marker id="small-head" viewBox="0 0 24 24" refX="20" refY="12" markerWidth="24" markerHeight="24" markerUnits="userSpaceOnUse" orient="auto-start-reverse">
      <path class="arrow-head" d="M0 0 L24 12 L0 24 Z"/>
    </marker>
    <marker id="hub-head" viewBox="0 0 60 60" refX="58" refY="30" markerWidth="60" markerHeight="60" markerUnits="userSpaceOnUse" orient="auto">
      <path class="arrow-head" d="M0 0 L60 30 L0 60 Z"/>
    </marker>
  </defs>

  <text class="chart-title" x="600" y="146" text-anchor="middle">vireLattice</text>

  <!-- links between neighbouring teams -->
  <g class="team-links">
    <path class="link-arrow" d="M556 272 Q600 262 644 272" marker-start="url(#small-head)" marker-end="url(#small-head)"/>
    <path class="link-arrow" d="M822 374 Q846 408 860 448" marker-start="url(#small-head)" marker-end="url(#small-head)"/>
    <path class="link-arrow" d="M860 652 Q846 692 822 726" marker-start="url(#small-head)" marker-end="url(#small-head)"/>
    <path class="link-arrow" d="M644 828 Q600 838 556 828" marker-start="url(#small-head)" marker-end="url(#small-head)"/>
    <path class="link-arrow" d="M378 726 Q354 692 340 652" marker-start="url(#small-head)" marker-end="url(#small-head)"/>
    <path class="link-arrow" d="M340 448 Q354 408 378 374" marker-start="url(#small-head)" marker-end="url(#small-head)"/>
  </g>

  <!-- central hub -->
  <g class="hub">
    <line class="hub-spoke" x1="600" y1="548" x2="745" y2="548" marker-end="url(#hub-head)"/>
    <line class="hub-spoke" x1="600" y1="548" x2="455" y2="548" marker-end="url(#hub-head)"/>
    <line class="hub-spoke" x1="600" y1="548" x2="672" y2="424" marker-end="url(#hub-head)"/>
    <line class="hub-spoke" x1="600" y1="548" x2="528" y2="424" marker-end="url(#hub-head)"/>
    <line class="hub-spoke" x1="600" y1="548" x2="672" y2="672" marker-end="url(#hub-head)"/>
    <line class="hub-spoke" x1="600" y1="548" x2="528" y2="672" marker-end="url(#hub-head)"/>
  </g>

  <!-- teams -->
  <g class="team team-sales">
    <circle class="team-ring" cx="460" cy="310" r="88"/>
    <text class="team-label" x="460"><tspan x="460" y="285">Team</tspan><tspan x="460" y="307">Sales &amp;</tspan><tspan x="460" y="329">Consulting</tspan></text>
  </g>
  <g class="team team-product">
    <circle class="team-ring" cx="740" cy="310" r="88"/>
    <text class="team-label"><tspan x="740" y="285">Team</tspan><tspan x="740" y="307">Product</tspan><tspan x="740" y="329">Management</tspan></text>
  </g>
  <g class="team team-supply">
    <circle class="team-ring" cx="878" cy="550" r="88"/>
    <text class="team-label"><tspan x="878" y="535">Team</tspan><tspan x="878" y="557">Supply</tspan><tspan x="878" y="579">Chain</tspan></text>
  </g>
  <g class="team team-hr">
    <circle class="team-ring" cx="740" cy="792" r="88"/>
    <text class="team-label"><tspan x="740" y="769">Team</tspan><tspan x="740" y="791">Human</tspan><tspan x="740" y="813">Resources</tspan></text>
  </g>
  <g class="team team-digital">
    <circle class="team-ring" cx="460" cy="792" r="88"/>
    <text class="team-label"><tspan x="460" y="769">Team</tspan><tspan x="460" y="791">Smart Digital</tspan><tspan x="460" y="813">Development</tspan></text>
  </g>
  <g class="team team-marketing">
    <circle class="team-ring" cx="322" cy="550" r="88"/>
    <text class="team-label"><tspan x="322" y="524">Team</tspan><tspan x="322" y="546">Marketing &amp;</tspan><tspan x="322" y="568">Communication</tspan></text>
  </g>
</svg>
</body>
</html>
```